I had to make an update to properly guide your designs.
I need a brochure for a company called Brevant Oakmere Ltd. all details you need can be found in the attached files including content in a microsoft word file. in the word file you will see the content you need please use them. you can. It is a consulting, construction and real estate company. You are free to add other relevant picture of yours that can make more sense. i have also attached the pictures needed. the word file show the usage of the pictures and the required content for them. It is pertinent to keep the design professional.
please be creative without the design appearing too crowded.
Updates
I had to make an update to properly guide your designs. i have attached a microsoft word file and pictures

```html
<!DOCTYPE html>
<html lang="en">
<head>
<meta charset="utf-8">
<title>Brevant Oakmere Ltd. — Our Services</title>
<link rel="stylesheet" href="https://fonts.googleapis.com/css2?family=Arimo:wght@400;700&family=Cinzel:wght@400&display=swap">
<style>
  :root {
    --red-deep: #9e1419;
    --red: #c0222a;
    --red-bright: #d8333a;
    --red-warm: #e0463f;
    --white: #ffffff;
    --pink-line: #f1a9a7;
    --bullet: #f39b97;
    --ring: #f07a75;
  }
  * { margin: 0; padding: 0; box-sizing: border-box; }
  html, body { width: 848px; height: 1200px; overflow: hidden; }
  body { font-family: "Arimo", Arial, sans-serif; color: var(--white); }

  .brochure-page {
    position: relative;
    width: 848px;
    height: 1200px;
    overflow: hidden;
    background: linear-gradient(180deg, var(--red-deep) 0%, var(--red) 30%, var(--red-bright) 55%, var(--red-warm) 100%);
  }
  .backdrop-photo {
    position: absolute;
    left: 0; right: 0; top: 480px; bottom: 0;
    background:
      linear-gradient(180deg,
        rgba(176,24,30,0) 0%,
        rgba(176,24,30,0.18) 30%,
        rgba(170,22,28,0.38) 65%,
        rgba(160,20,26,0.5) 100%),
      radial-gradient(ellipse at 25% 100%, rgba(235,90,84,0.35) 0%, rgba(235,90,84,0) 60%);
  }
  .column-divider {
    position: absolute;
    left: 503px; top: 0; bottom: 0;
    width: 1px;
    background: rgba(255,255,255,0.75);
  }

  .services-title {
    position: absolute;
    left: 51px; top: 44px;
    font-family: "Cinzel", Georgia, serif;
    font-weight: 400;
    font-size: 30px;
    letter-spacing: 1px;
  }
  .services-title-rule {
    position: absolute;
    left: 51px; top: 80px;
    width: 441px; height: 1px;
    background: rgba(255,255,255,0.7);
  }

  .service-heading {
    position: absolute;
    left: 51px;
    font-weight: 700;
    font-size: 18px;
    letter-spacing: 0.3px;
  }
  .service-list {
    position: absolute;
    left: 51px;
    list-style: none;
    font-size: 11.5px;
  }
  .service-list li {
    position: relative;
    padding-left: 27px;
    height: 22.5px;
    line-height: 22.5px;
  }
  .service-list li::before {
    content: "";
    position: absolute;
    left: 5px; top: 9px;
    width: 4px; height: 4px;
    border-radius: 50%;
    background: var(--bullet);
  }

  .service-photo {
    position: absolute;
    left: 51px;
    width: 441px;
  }
  .photo-consulting {
    top: 371px; height: 173px;
    border-radius: 0 0 36px 0;
    background: linear-gradient(170deg, #b4b4a8 0%, #8e8266 40%, #7a6a4c 70%, #5f7a4a 100%);
  }
  .photo-construction {
    top: 724px; height: 174px;
    border-radius: 0 0 36px 0;
    background: linear-gradient(180deg, #dfe3e6 0%, #c9cbc9 35%, #a9a69f 70%, #8f8b82 100%);
  }
  .photo-realestate {
    top: 972px; height: 164px;
    border-radius: 0 36px 0 0;
    background: linear-gradient(180deg, #dde4ea 0%, #d4d2c8 50%, #9aa08a 80%, #6f7560 100%);
  }

  .sector-card { position: absolute; left: 509px; width: 327px; }
  .sector-image {
    position: absolute;
    left: 71px;
    width: 143px; height: 143px;
    border-radius: 50%;
    border: 3px solid var(--ring);
  }
  .sector-label {
    position: absolute;
    left: 0;
    font-weight: 700;
    font-size: 11.5px;
  }
  .sector-rule {
    position: absolute;
    left: 0;
    width: 327px; height: 1px;
    background: var(--pink-line);
  }
  .img-building { background: linear-gradient(200deg, #8fb6e0 0%, #3f6b9a 55%, #1e3550 100%); }
  .img-flood { background: radial-gradient(circle at 50% 40%, #d9dde0 0%, #8a9096 50%, #3d4349 100%); }
  .img-canal { background: linear-gradient(180deg, #dfe3e6 0%, #b17a4f 40%, #8a5a3a 75%, #6d5a44 100%); }
  .img-geo { background: linear-gradient(160deg, #c8c7bd 0%, #9a9a8e 50%, #6b7268 100%); }
  .img-highway { background: linear-gradient(180deg, #e6e8ea 0%, #9aa0a6 45%, #b33a34 80%, #7a5d48 100%); }
  .img-environment { background: linear-gradient(120deg, #e2e4e6 0%, #7d8389 50%, #2f353b 100%); }
</style>
</head>
<body>
<main class="brochure-page">
  <div class="backdrop-photo" role="img" aria-label="Faded photo of red steel trench shoring at a construction site"></div>
  <div class="column-divider"></div>

  <h1 class="services-title">Our Services</h1>
  <div class="services-title-rule"></div>

  <h2 class="service-heading" style="top:101px;">CONSULTING</h2>
  <ul class="service-list" style="top:122px;">
    <li>Road design</li>
    <li>Building structural design</li>
    <li>Storm and waste water sewer systems</li>
    <li>Large expanse drainage network design</li>
    <li>Infrastructure planning for large area (hectarage) property developments</li>
    <li>Flood assessment, mitigation and river engineering hydraulic modelling</li>
    <li>Lidar survey, contour mapping, Terrain modelling.</li>
    <li>Wastewater treatment system</li>
    <li>Mechanical and electrical infrastructure design</li>
    <li>Project management</li>
    <li>Area terrain photography and video</li>
  </ul>
  <div class="service-photo photo-consulting" role="img" aria-label="Earthworks crew building a drainage channel beside a new road"></div>

  <h2 class="service-heading" style="top:564px;">CONSTRUCTION</h2>
  <ul class="service-list" style="top:583px;">
    <li>Road construction</li>
    <li>Commercial and residential Building Construction</li>
    <li>Storm water drainage construction</li>
    <li>Sewer networks and treatment plant construction</li>
    <li>Civil works construction.</li>
    <li>Electrification.</li>
  </ul>
  <div class="service-photo photo-construction" role="img" aria-label="Newly paved interlocking block road on a development site"></div>

  <h2 class="service-heading" style="top:906px;">REAL ESTATE</h2>
  <ul class="service-list" style="top:927px;">
    <li>Commercial property development and lease/sale</li>
    <li>Residential property development and lease/sale</li>
  </ul>
  <div class="service-photo photo-realestate" role="img" aria-label="Rendering of a modern multi-storey residential building"></div>

  <section class="sector-card" style="top:48px;">
    <div class="sector-image img-building" role="img" aria-label="Glass office tower against blue sky"></div>
    <span class="sector-label" style="top:156px;">Building Engineering</span>
    <div class="sector-rule" style="top:174px;"></div>
  </section>
  <section class="sector-card" style="top:236px;">
    <div class="sector-image img-flood" role="img" aria-label="Flooded tunnel interior"></div>
    <span class="sector-label" style="top:152px;">Flood Risk Management</span>
    <div class="sector-rule" style="top:170px;"></div>
  </section>
  <section class="sector-card" style="top:420px;">
    <div class="sector-image img-canal" role="img" aria-label="Excavated canal with water"></div>
    <span class="sector-label" style="top:150px;">Canal and Waterway</span>
    <div class="sector-rule" style="top:168px;"></div>
  </section>
  <section class="sector-card" style="top:605px;">
    <div class="sector-image img-geo" role="img" aria-label="Aerial view of a highway interchange"></div>
    <span class="sector-label" style="top:149px;">Geospatial Solutions</span>
    <div class="sector-rule" style="top:167px;"></div>
  </section>
  <section class="sector-card" style="top:790px;">
    <div class="sector-image img-highway" role="img" aria-label="Tipper truck unloading at a road works site"></div>
    <span class="sector-label" style="top:147px;">Highway Engineering</span>
    <div class="sector-rule" style="top:165px;"></div>
  </section>
  <section class="sector-card" style="top:975px;">
    <div class="sector-image img-environment" role="img" aria-label="Screw pumps at a wastewater treatment plant"></div>
    <span class="sector-label" style="top:145px;">Environmental</span>
    <div class="sector-rule" style="top:163px;"></div>
  </section>
</main>
</body>
</html>
```